Business card design for Plumbing and Gas fitting company

We need a business card design for our plumbing and gas fitting company using the company logo and director details. Design should be modern and eye-catching however kept reasonably simple. This design should be targeted at commercial businesses/work so professionalism is key.

Target Market(s)

Commercial/business

Industry/Entity Type

Plumbing

Contact Information for Business Card

Warren Dohey
Director
027 581 9043
warren@vantorplumbingandgas.example
PO Box 7816
Palmerston North 4472

Font styles to use
Sans Serif

Requirements
Must have
• Logo
• Modern
• Kept simple
Nice to have
• Colour scheme based around logo

```html
<!DOCTYPE html>
<html lang="en">
<head>
<meta charset="utf-8">
<title>Vantor Plumbing &amp; Gas – Business Card</title>
<link rel="stylesheet" href="https://fonts.googleapis.com/css2?family=Roboto:wght@400;500;700&display=swap">
<style>
  :root {
    --bg-dark: #4d5559;
    --bg-light: #7c858a;
    --card-white: #ffffff;
    --card-grey: #7a7a7a;
    --brand-blue: #1467b3;
    --brand-orange: #e9782f;
    --text-light: #ffffff;
    --text-soft: #ececec;
  }
  * { margin: 0; padding: 0; box-sizing: border-box; }
  html, body { width: 1200px; height: 900px; overflow: hidden; }
  body {
    font-family: "Roboto", Arial, sans-serif;
    background: radial-gradient(ellipse at 50% 45%, var(--bg-light), var(--bg-dark));
    position: relative;
  }
  .card {
    position: absolute;
    left: 250px;
    width: 700px;
    height: 400px;
    border-radius: 22px;
    overflow: hidden;
    background: var(--card-white);
    box-shadow: 0 14px 30px rgba(0,0,0,0.35);
  }
  .card--front { top: 470px; }
  .card--back { top: 40px; }

  .card__shapes { position: absolute; inset: 0; }

  .brand {
    position: absolute;
    display: flex;
    align-items: center;
    gap: 12px;
  }
  .brand__dot {
    width: 26px; height: 26px; border-radius: 50%;
    background: var(--brand-orange);
    flex: none;
  }
  .brand__name {
    font-weight: 700;
    color: var(--brand-blue);
    white-space: nowrap;
    letter-spacing: 0.2px;
  }
  .card--front .brand {
    left: 50%; top: 50%;
    transform: translate(-50%, -50%);
  }
  .card--front .brand__name { font-size: 40px; }
  .card--back .brand { right: 44px; top: 176px; }
  .card--back .brand__name { font-size: 26px; }
  .card--back .brand__dot { width: 18px; height: 18px; }

  .contact {
    position: absolute;
    left: 46px; top: 44px;
    color: var(--text-light);
  }
  .contact__name { font-size: 28px; font-weight: 700; }
  .contact__role { font-size: 15px; color: var(--text-soft); margin-top: 2px; }
  .contact__address {
    margin-top: 22px;
    font-size: 16px; line-height: 1.45;
    color: var(--text-soft);
  }
  .contact__line { display: flex; align-items: center; gap: 8px; }
  .contact__icon { width: 14px; height: 14px; flex: none; fill: var(--text-light); }
  .contact__email {
    position: absolute;
    left: 46px; bottom: 40px;
    font-size: 13px; color: var(--text-soft);
    white-space: nowrap;
  }
</style>
</head>
<body>

  <section class="card card--back">
    <svg class="card__shapes" viewBox="0 0 700 400" width="700" height="400" aria-hidden="true">
      <rect width="700" height="400" fill="var(--card-grey)"/>
      <path d="M470 0 Q250 150 370 400" fill="none" stroke="var(--brand-blue)" stroke-width="6"/>
      <path d="M484 0 Q268 150 386 400 L700 400 L700 0 Z" fill="var(--card-white)"/>
    </svg>

    <div class="contact">
      <div class="contact__name">Warren Dohey</div>
      <div class="contact__role">Director</div>
      <div class="contact__address">
        <div class="contact__line"><span>PO Box 7816</span></div>
        <div class="contact__line"><span>Palmerston North 4472</span></div>
        <div class="contact__line">
          <svg class="contact__icon" viewBox="0 0 24 24" aria-hidden="true"><path d="M6.6 10.8a15.1 15.1 0 0 0 6.6 6.6l2.2-2.2c.3-.3.7-.4 1-.2 1.1.4 2.3.6 3.6.6.6 0 1 .4 1 1V20c0 .6-.4 1-1 1A17 17 0 0 1 3 4c0-.6.4-1 1-1h3.5c.6 0 1 .4 1 1 0 1.3.2 2.5.6 3.6.1.3 0 .7-.2 1z"/></svg>
          <span>027 581 9043</span>
        </div>
      </div>
    </div>

    <div class="contact__email contact__line">
      <svg class="contact__icon" viewBox="0 0 24 24" aria-hidden="true"><path d="M3 5h18v14H3zM4.5 6.5 12 12l7.5-5.5z"/></svg>
      <span>warren@vantorplumbingandgas.example</span>
    </div>

    <div class="brand">
      <span class="brand__dot"></span>
      <span class="brand__name">Vantor Plumbing &amp; Gas</span>
    </div>
  </section>

  <section class="card card--front">
    <div class="brand">
      <span class="brand__dot"></span>
      <span class="brand__name">Vantor Plumbing &amp; Gas</span>
    </div>
  </section>

</body>
</html>
```